Need a simple blog where questions can be posted and answered by the community. I already have something started in WordPress. www.brimfernalerts.com. I cannot figure out how to make the blog functionality work the way I want. It is IMPORTANT the designer code it in the existing wordpress account.

```html
<!DOCTYPE html>
<html lang="en">
<head>
<meta charset="utf-8">
<title>Brimfern — COVID-19 Partner &amp; Industry Forum</title>
<link href="https://fonts.googleapis.com/css2?family=Source+Sans+3:wght@400;600;700&display=swap" rel="stylesheet">
<style>
  :root {
    --navy: #0b3a5e;
    --navy-deep: #0d2c47;
    --ink: #111111;
    --body-grey: #6b6b6b;
    --white: #ffffff;
    --card-line: #e2e2e2;
  }
  * { box-sizing: border-box; margin: 0; padding: 0; }
  html, body { width: 1200px; height: 2338px; overflow: hidden; }
  body {
    position: relative;
    background: var(--white);
    font-family: "Source Sans 3", "Source Sans Pro", Arial, sans-serif;
    color: var(--ink);
  }

  .hero {
    position: absolute; left: 0; top: 0; width: 1200px; height: 535px;
    background: linear-gradient(180deg, #17384f 0%, #1b4363 45%, #16344d 100%);
    color: var(--white); text-align: center;
  }
  .brand {
    position: absolute; left: 0; right: 0;
    display: flex; align-items: center; justify-content: center; gap: 12px;
    font-weight: 700; letter-spacing: 2px;
  }
  .brand-square { display: block; background: var(--white); }
  .hero .brand { top: 178px; font-size: 34px; }
  .hero .brand-square { width: 34px; height: 34px; }
  .hero-title {
    position: absolute; left: 0; right: 0; top: 311px;
    font-size: 35px; font-weight: 700; letter-spacing: 0.3px;
  }
  .hero-text {
    position: absolute; left: 0; right: 0; top: 372px;
    font-size: 16.5px; line-height: 23.6px;
  }

  .main-nav {
    position: absolute; left: 0; top: 535px; width: 1200px; height: 75px;
    background: var(--navy);
    display: flex; align-items: center; gap: 27px; padding-left: 59px;
  }
  .main-nav a {
    color: var(--white); text-decoration: none;
    font-size: 19.5px; font-weight: 600; letter-spacing: 0.2px;
  }

  .post-card {
    position: absolute; left: 60px; width: 705px; height: 284px;
    background: var(--white);
    box-shadow: 0 0 4px rgba(0,0,0,0.18);
    display: flex;
  }
  .post-photo { width: 286px; height: 100%; flex: none; }
  .post-body { padding: 48px 0 0 38px; }
  .post-title { font-size: 36px; font-weight: 700; line-height: 40px; }
  .post-meta { font-size: 11px; margin-top: 8px; color: #222; }
  .post-excerpt {
    font-size: 16.5px; line-height: 23.6px; color: var(--body-grey);
    margin-top: 4px;
  }

  .side-box {
    position: absolute; left: 807px; width: 332px;
    background: var(--white);
    box-shadow: 0 0 4px rgba(0,0,0,0.18);
    padding: 58px 28px 0 28px;
  }
  .side-title { font-size: 23.6px; font-weight: 700; line-height: 25px; }
  .side-text {
    font-size: 15.5px; line-height: 23.6px; color: var(--body-grey);
    margin-top: 12px;
  }

  .promo-box {
    position: absolute; left: 807px; top: 1074px; width: 332px; height: 657px;
    background: var(--navy); color: var(--white); text-align: center;
  }
  .promo-box .brand { top: 120px; font-size: 24px; }
  .promo-box .brand-square { width: 24px; height: 24px; }
  .promo-title {
    position: absolute; left: 0; right: 0; top: 268px;
    font-size: 23.6px; font-weight: 700; line-height: 25.5px;
  }
  .promo-text {
    position: absolute; left: 0; right: 0; top: 344px;
    font-size: 15px; line-height: 23.6px;
  }
  .promo-button {
    position: absolute; left: 89px; top: 494px; width: 154px; height: 50px;
    background: var(--white); color: var(--navy-deep);
    display: flex; align-items: center; justify-content: center;
    font-size: 14.5px; font-weight: 700; letter-spacing: 0.4px;
    text-decoration: none;
  }
</style>
</head>
<body>

<header class="hero">
  <div class="brand"><span class="brand-square"></span>BRIMFERN</div>
  <h1 class="hero-title">COVID-19 PARTNER &amp; INDUSTRY FORUM</h1>
  <p class="hero-text">Lorem ipsum dolor sit amet, consectetur adipiscing elit, sed do eiusmod tempor<br>incididunt ut labore et dolore magna aliqua. Ut enim ad minim veniam,<br>quis nostrud exercitation ullamco laboris</p>
</header>

<nav class="main-nav">
  <a href="#">HOME</a>
  <a href="#">UPDATES</a>
  <a href="#">NEWS</a>
  <a href="#">COVID-19</a>
  <a href="#">PARTNERS</a>
</nav>

<article class="post-card" style="top:705px">
  <div class="post-photo" role="img" aria-label="Woman in a face mask picking tomatoes at a grocery shelf" style="background:linear-gradient(135deg,#8fb86a 0%,#c9472e 45%,#2e2c2c 75%,#3b8a7a 100%)"></div>
  <div class="post-body">
    <h2 class="post-title">Dummy Question ?</h2>
    <p class="post-meta">March 2020 by admin</p>
    <p class="post-excerpt">Lorem ipsum dolor sit amet, consectetur<br>adipiscing elit, sed do eiusmod tempor<br>incididunt ut labore et dolore magna<br>aliqua. Ut enim ad minim veniam,<br>quis nostrud exercitation ullamco laboris</p>
  </div>
</article>

<aside class="side-box" style="top:706px;height:284px">
  <h3 class="side-title">About Us</h3>
  <p class="side-text">Lorem ipsum dolor sit amet,<br>consectetur adipiscing elit, sed<br>do eiusmod tempor incididunt ut<br>labore et dolore magna aliqua.<br>Ut enim ad minim veniam, quis<br>nostrud exercitation ullamco laboris</p>
</aside>

<article class="post-card" style="top:1074px">
  <div class="post-photo" role="img" aria-label="Hands pouring hand sanitiser from a small bottle" style="background:linear-gradient(135deg,#5e0d10 0%,#a3141c 50%,#d9c7c0 100%)"></div>
  <div class="post-body">
    <h2 class="post-title">Dummy Question ?</h2>
    <p class="post-meta">March 2020 by admin</p>
    <p class="post-excerpt">Lorem ipsum dolor sit amet, consectetur<br>adipiscing elit, sed do eiusmod tempor<br>incididunt ut labore et dolore magna<br>aliqua. Ut enim ad minim veniam,<br>quis nostrud exercitation ullamco laboris</p>
  </div>
</article>

<aside class="promo-box">
  <div class="brand"><span class="brand-square"></span>BRIMFERN</div>
  <h3 class="promo-title">COVID-19 PARTNER &amp;<br>INDUSTRY FORUM</h3>
  <p class="promo-text">Lorem ipsum dolor sit amet, consectetur<br>adipiscing elit, sed do eiusmod tempor<br>incididunt ut labore et dolore magna<br>aliqua. Ut enim ad minim veniam,<br>quis nostrud exercitation ullamco laboris</p>
  <a class="promo-button" href="#">KNOW MORE</a>
</aside>

<article class="post-card" style="top:1448px">
  <div class="post-photo" role="img" aria-label="Lightbox sign on a wooden stool against an orange wall" style="background:linear-gradient(180deg,#e9673a 0%,#e2dfe0 35%,#dcdadb 60%,#a86a3d 80%,#e9673a 100%)"></div>
  <div class="post-body">
    <h2 class="post-title">Dummy Question ?</h2>
    <p class="post-meta">March 2020 by admin</p>
    <p class="post-excerpt">Lorem ipsum dolor sit amet, consectetur<br>adipiscing elit, sed do eiusmod tempor<br>incididunt ut labore et dolore magna<br>aliqua. Ut enim ad minim veniam,<br>quis nostrud exercitation ullamco laboris</p>
  </div>
</article>

<article class="post-card" style="top:1815px">
  <div class="post-photo" role="img" aria-label="Person holding a stay-home paper sign against a red wall" style="background:linear-gradient(180deg,#c8401f 0%,#e8e6e3 45%,#e0ddd9 65%,#b83a1c 100%)"></div>
  <div class="post-body">
    <h2 class="post-title">Dummy Question ?</h2>
    <p class="post-meta">March 2020 by admin</p>
    <p class="post-excerpt">Lorem ipsum dolor sit amet, consectetur<br>adipiscing elit, sed do eiusmod tempor<br>incididunt ut labore et dolore magna<br>aliqua. Ut enim ad minim veniam,<br>quis nostrud exercitation ullamco laboris</p>
  </div>
</article>

<aside class="side-box" style="top:1815px;height:284px">
  <h3 class="side-title">Know More About<br>COVID-19</h3>
  <p class="side-text">Lorem ipsum dolor sit amet,<br>consectetur adipiscing elit, sed<br>do eiusmod tempor incididunt ut<br>labore et dolore magna aliqua.<br>Ut enim ad minim veniam</p>
</aside>

</body>
</html>
```